Industrial Company needing new business cards

We are a newly branded Industrial trade company. We specialise in Electrical, Mechanical and Air-conditioning.

I would like to see designs single sided. Focusing on the color scheme white/red/black and possibly gray. Possibly make it a black card with white writting... but open to all designs.

I would like the design to be professional, sleek and to the point.

Industry/Entity Type

Business

Contact Information for Business Card

Tom Harwick
Managing Director / Electrician
tomwork@velnet.com.au
47 Garnet Road, Rutherford NSW 2320
Mobile: 0427115830
www.harwickindustrialgroup.com.au

Requirements
Must have
• Must be able to be sent in a manner that i can change the details for each employee.
• Our logo
Nice to have
• Would like it to somehow have " incorporating Talvo Group Pty Ltd" as this is the company we have taken over.
Should not have
• No yellow!!!
• must not simply place "talvo group" randomly on the business card. refer nice to have.

```html
<!DOCTYPE html>
<html lang="en">
<head>
<meta charset="utf-8">
<title>Harwick Industrial Group – Business Card</title>
<link rel="stylesheet" href="https://fonts.googleapis.com/css2?family=Open+Sans:ital,wght@0,400;0,600;0,700;1,400&display=swap">
<style>
  :root {
    --stage: #3b3b3b;
    --card-black: #050505;
    --card-glow: #2a2a2a;
    --brand-red: #e0000f;
    --white: #ffffff;
    --soft-white: #e6e6e6;
    --band-white: #f2f2f2;
  }
  * { box-sizing: border-box; margin: 0; padding: 0; }
  html, body {
    width: 1200px; height: 750px; overflow: hidden;
    background: var(--stage);
    font-family: "Open Sans", Arial, sans-serif;
  }
  .sheet { position: relative; width: 1200px; height: 750px; }
  .card {
    position: absolute; top: 228px;
    width: 461px; height: 263px; overflow: hidden;
    background: var(--card-black);
  }
  .card--front { left: 124px; }
  .card--back { left: 618px; }

  .texture { position: absolute; }
  .card--front .texture {
    left: 150px; top: -40px; width: 320px; height: 280px;
    background: radial-gradient(ellipse at center, var(--card-glow) 0%, rgba(20,20,20,0.6) 40%, rgba(5,5,5,0) 70%);
  }
  .card--back .texture {
    left: 40px; top: -20px; width: 360px; height: 300px;
    background: radial-gradient(ellipse at center, var(--card-glow) 0%, rgba(20,20,20,0.6) 40%, rgba(5,5,5,0) 70%);
  }

  .wordmark {
    position: absolute; color: var(--white);
    font-weight: 700; text-transform: uppercase; line-height: 1.1;
  }
  .card--front .wordmark { left: 300px; top: 50px; font-size: 14px; letter-spacing: 0.5px; }
  .card--back .wordmark { left: 44px; top: 160px; font-size: 17px; letter-spacing: 0.5px; }

  .accent-tab {
    position: absolute; left: 0; top: 141px; width: 6px; height: 29px;
    background: var(--brand-red);
  }
  .person-name {
    position: absolute; left: 25px; top: 143px;
    color: var(--brand-red); font-size: 15.5px; font-weight: 600;
  }
  .person-role {
    position: absolute; left: 25px; top: 163px;
    color: var(--soft-white); font-size: 12px; font-weight: 400;
  }
  .role-rule {
    position: absolute; left: 206px; top: 167px; width: 232px; height: 1px;
    background: var(--soft-white);
  }
  .contact-list { position: absolute; left: 28px; top: 186px; list-style: none; }
  .contact-item {
    display: flex; align-items: center; height: 17.5px;
    color: var(--white); font-size: 10.5px;
  }
  .contact-icon { width: 11px; height: 11px; margin-right: 5px; flex: none; }

  .footer-band { position: absolute; left: 0; bottom: 0; width: 461px; height: 10px; }

  .web-address {
    position: absolute; left: 41px; top: 222px;
    color: var(--soft-white); font-size: 11px; font-style: italic; letter-spacing: 2.2px;
  }
  .corner-panel { position: absolute; right: 0; top: 0; width: 226px; height: 263px; }
</style>
</head>
<body>
<main class="sheet">

  <section class="card card--front" aria-label="Business card front">
    <div class="texture" role="img" aria-label="Dark metal mesh texture"></div>
    <div class="wordmark">Harwick<br>Industrial<br>Group</div>

    <div class="accent-tab"></div>
    <h1 class="person-name">Tom Harwick</h1>
    <p class="person-role">Managing Director / Electrician</p>
    <div class="role-rule"></div>

    <ul class="contact-list">
      <li class="contact-item">
        <svg class="contact-icon" viewBox="0 0 11 11"><rect x="2.5" y="0.5" width="6" height="10" rx="1" fill="none" stroke="var(--brand-red)" stroke-width="1.4"/><rect x="4.5" y="8" width="2" height="1" fill="var(--brand-red)"/></svg>
        0427115830
      </li>
      <li class="contact-item">
        <svg class="contact-icon" viewBox="0 0 11 11"><rect x="0.5" y="2" width="10" height="7" fill="var(--brand-red)"/><path d="M0.5 2 L5.5 6 L10.5 2" fill="none" stroke="var(--card-black)" stroke-width="1"/></svg>
        tomwork@velnet.com.au
      </li>
      <li class="contact-item">
        <svg class="contact-icon" viewBox="0 0 11 11"><circle cx="5.5" cy="5.5" r="5" fill="var(--brand-red)"/><path d="M3 3.5 Q5 3 5 5 Q4 7 3 6 Z M6.5 6 Q8.5 5.5 8 8 Q6.5 8.5 6.5 6 Z" fill="var(--card-black)"/></svg>
        harwickindustrialgroup.com.au
      </li>
    </ul>

    <svg class="footer-band" viewBox="0 0 461 10" preserveAspectRatio="none">
      <polygon points="0,0 301,0 297,10 0,10" fill="var(--brand-red)"/>
      <polygon points="304,0 461,0 461,10 300,10" fill="var(--band-white)"/>
    </svg>
  </section>

  <section class="card card--back" aria-label="Business card back">
    <div class="texture" role="img" aria-label="Dark metal mesh texture"></div>
    <svg class="corner-panel" viewBox="0 0 226 263" preserveAspectRatio="none">
      <polygon points="0,0 226,0 226,263" fill="var(--brand-red)"/>
    </svg>
    <div class="wordmark">Harwick<br>Industrial<br>Group</div>
    <p class="web-address">www.harwickindustrialgroup.com.au</p>
  </section>

</main>
</body>
</html>
```